"The Wandering Mentor", a Higher Ed blogger, would like a wordpress design

I would like a wordpress design for blogs written by "The Wandering Mentor." that can be easily expanded by me once the initial design is complete.

Here is context which I would like included on the Home/Welcome page: "I started The Wandering Mentor in 2021 to write about the practice of academic advising through the lens of horsemanship. After one year of developing skills as a brand new equestrian, I couldn’t help but notice the similarities between my vocation as an academic advisor and my avocation as a budding equestrian. I hope my musings about my journey in two very different fields will cultivate curiosity, widen your aperture and ignite academic advisors to take their practice to the next level. "

The wordpress will primarily have blogs by myself or guest bloggers writing about academic advising for advisors, but I may widen my audience to include students and families. I'd like to have readers submit questions that I can answer. Depending on interest, I may want to have a section on Horsemanship but that is not truly the focus of this site.

I'd like the feel of the site to be positive, fresh, modern (but not too wild), with the emphasis on Higher Ed/Academic Advising as opposed to equestrian pursuits. I don't want it to feel clunky and blocky like some sites that have to do with education. I'm hoping that readers will have some "aha" moments after reading some of the posts.

I have included my logo files

```html
<!DOCTYPE html>
<html lang="en">
<head>
<meta charset="utf-8">
<title>The Wandering Mentor – Home Page Layouts</title>
<link rel="stylesheet" href="https://fonts.googleapis.com/css2?family=Montserrat:wght@400;600;700&family=Lato:wght@400;700&family=Comfortaa:wght@400&family=Libre+Baskerville&display=swap">
<style>
:root{
  --stage:#4b4b4b;
  --ink:#0b0b0b;
  --bar:#141414;
  --panel:#1d1b1c;
  --gold:#d7a964;
  --gold-soft:#e2bd82;
  --sand:#dcb073;
  --white:#ffffff;
  --dark-text:#1b1b1b;
  --heading:Montserrat,sans-serif;
  --body:Lato,sans-serif;
}
*{box-sizing:border-box;margin:0;padding:0}
html,body{width:1200px;height:2404px;overflow:hidden;background:var(--stage)}
.stage{position:relative;width:1286px;height:2576px;transform:scale(.93313);transform-origin:0 0}
.presentation-title{position:absolute;left:0;width:1286px;top:100px;text-align:center}
.presentation-title .mark{width:110px;height:110px;border:3px solid var(--white);border-radius:50%;margin:0 auto 20px}
.presentation-title h1{font-family:Comfortaa,sans-serif;font-weight:400;color:var(--white);font-size:33px;letter-spacing:.5px}

.page{position:absolute;overflow:hidden;background:var(--ink);font-family:var(--body);color:var(--white)}
.page *{position:absolute}
.page--desktop{top:714px;width:460px;height:1174px}
.page--a{left:72px}
.page--b{left:561px}
.page--mobile{left:1049px;top:714px;width:127px;height:1848px}
.top-bar{left:0;top:0;width:100%;height:14px;background:var(--bar)}
.social{top:3px;width:8px;height:8px;border:1px solid var(--white);border-radius:50%}
.contact-line{top:4px;right:52px;font-size:4.6px;white-space:nowrap}
.contact-line span{position:static;margin-left:10px}
.brand-badge{left:0;width:100%;top:22px;text-align:center;font-family:var(--heading);font-size:6px;font-weight:600;color:var(--gold)}
.brand-badge i{position:static;display:inline-block;width:7px;height:7px;border:1px solid var(--gold);border-radius:50%;vertical-align:middle;margin-right:3px}
.main-nav{top:56px;left:0;width:100%;text-align:center;font-family:var(--heading);font-size:4.6px;font-weight:600}
.main-nav a{position:static;color:var(--white);text-decoration:none;margin:0 7px}
.main-nav a.is-active{color:var(--gold)}
.hero-title{left:0;width:100%;top:134px;text-align:center;font-family:var(--heading);font-weight:700;font-size:20.5px;color:var(--gold);letter-spacing:.3px}
.hero-sub{left:0;width:100%;top:164px;text-align:center;font-size:4.7px}
.slider-dots{left:0;width:100%;text-align:center;font-size:0}
.slider-dots i{position:static;display:inline-block;width:5px;height:5px;border:1px solid var(--white);border-radius:50%;margin:0 1px}
.slider-dots i.on{background:var(--white)}
.wave{left:0;width:100%}
.welcome{left:0;width:100%;background:var(--panel)}
.welcome-art{border-radius:6px;background:linear-gradient(135deg,#2a2622,#3b3124 60%,#2a2622)}
.eyebrow{font-family:var(--heading);font-weight:700;color:var(--gold)}
.welcome-heading{font-family:var(--heading);font-weight:700;color:var(--white)}
.rule{height:2px;width:22px;background:var(--gold);border-radius:1px}
.rule--dark{background:var(--dark-text)}
.welcome-copy{color:#e7e2dc;font-family:var(--body)}
.btn{background:var(--gold);color:var(--white);border-radius:10px;text-align:center;font-family:var(--heading);font-weight:700}
.blog{left:0;width:100%;background:linear-gradient(180deg,#dcb276,#d4a766 55%,#dcb276)}
.blog-heading{left:0;width:100%;text-align:center;font-family:var(--heading);font-weight:700;color:var(--dark-text)}
.post-card{background:var(--panel);border-radius:44px;text-align:center}
.post-photo{left:50%;transform:translateX(-50%);border-radius:50%}
.photo-1{background:linear-gradient(160deg,#c58a52,#8a5a3a 60%,#d9c3a9)}
.photo-2{background:linear-gradient(180deg,#7a8594,#c9c2b5 55%,#b39a7a)}
.photo-3{background:linear-gradient(160deg,#d8d6d2,#6b4a35 65%,#3d2c22)}
.photo-4{background:linear-gradient(160deg,#c26a3b,#6d3c28 60%,#e6b28b)}
.photo-5{background:linear-gradient(160deg,#5c4238,#9b7f6b 60%,#2e2420)}
.photo-6{background:linear-gradient(160deg,#7d8a7a,#404a44 55%,#cfd2cc)}
.post-date{left:50%;transform:translateX(-50%);border-radius:50%;background:var(--white);color:#333;font-size:2.6px;line-height:1.1;text-align:center;padding-top:3px}
.post-title{left:0;width:100%;color:var(--gold);font-family:var(--heading)}
.post-title b{position:static;display:block;font-weight:700}
.post-excerpt{left:0;width:100%;color:#eee}
.post-arrow{left:50%;transform:translateX(-50%);color:var(--gold)}
.footer{left:0;width:100%;background:var(--ink)}
.footer-heading{font-family:'Libre Baskerville',serif;font-weight:400;color:var(--white)}
.footer-links a{position:static;display:block;color:var(--white);text-decoration:none}
.divider-v{width:1px;background:#333}
.divider-h{height:1px;background:#3a3a3a}
.footer-brand{text-align:center;font-family:var(--heading);font-weight:600;color:var(--gold)}
.footer-brand i{position:static;display:block;margin:0 auto 8px;border:2px solid var(--gold);border-radius:50%}
.footer-contact{color:#ddd}
.footer-contact p{position:static}
.footer-contact .icon{position:static;color:var(--gold);margin-right:4px}
.legal{font-size:4.6px;color:#ccc;white-space:nowrap}
</style>
</head>
<body>
<div class="stage">

  <header class="presentation-title">
    <div class="mark"></div>
    <h1>The Wandering Mentor</h1>
  </header>

  <!-- Desktop layout A -->
  <section class="page page--desktop page--a">
    <div class="top-bar">
      <i class="social" style="left:55px"></i><i class="social" style="left:66px"></i><i class="social" style="left:77px"></i>
      <div class="contact-line"><span>Phone: 555-014-2290</span><span>Email: hello@wanderingmentor.demo</span></div>
    </div>
    <div class="brand-badge"><i></i>The Wandering Mentor</div>
    <nav class="main-nav"><a class="is-active">HOME</a><a>ABOUT</a><a>SERVICES</a><a>BLOGS</a><a>FAQS</a><a>BOOKINGS</a></nav>
    <h2 class="hero-title">THE WANDERING MENTOR</h2>
    <p class="hero-sub">Partnering With Academic Advisors In Moving Their Practice Forward</p>
    <div class="slider-dots" style="top:260px"><i></i><i class="on"></i><i></i><i></i></div>
    <svg class="wave" style="top:225px" width="460" height="90" viewBox="0 0 460 90">
      <path d="M0 90 L0 84 C80 78 150 68 200 50 C245 32 270 24 300 32 C345 46 390 62 460 68 L460 90Z" fill="#1d1b1c"/>
      <path d="M0 84 C80 78 150 68 200 50 C245 32 270 24 300 32 C345 46 390 62 460 68" fill="none" stroke="#d7a964" stroke-width="4"/>
    </svg>
    <div class="welcome" style="top:314px;height:206px">
      <div class="welcome-art" role="img" aria-label="Line illustration of a horse and rider jumping" style="left:28px;top:20px;width:210px;height:140px"></div>
      <p class="eyebrow" style="left:252px;top:14px;font-size:10.5px">WELCOME TO</p>
      <h3 class="welcome-heading" style="left:252px;top:30px;font-size:10.5px">THE WANDERING MENTOR</h3>
      <div class="rule" style="left:252px;top:47px"></div>
      <p class="welcome-copy" style="left:252px;top:60px;width:182px;font-size:4.9px;line-height:10.7px">I started The Wandering Mentor in 2021 to write about the practice of academic advising through the lens of horsemanship. After one year of developing skills as a brand new equestrian, I couldn't help but notice the similarities between my vocation as an academic advisor and my avocation as a budding equestrian. I hope my musings about my journey in two very different fields will cultivate curiosity, widen your aperture and ignite academic advisors to take their practice to the next level.</p>
      <div class="btn" style="left:252px;top:152px;width:68px;height:19px;line-height:19px;font-size:5.2px">LEARN MORE</div>
    </div>
    <div class="blog" style="top:520px;height:440px">
      <h3 class="blog-heading" style="top:32px;font-size:11.5px">OUR LATEST BLOG</h3>
      <div class="rule rule--dark" style="left:219px;top:50px"></div>

      <article class="post-card" style="left:77px;top:68px;width:88px;height:152px"><div class="post-photo photo-1" role="img" aria-label="Rider hugging a horse" style="top:4px;width:80px;height:80px"></div><div class="post-date" style="top:74px;width:15px;height:15px">15 sep<br>2021</div><p class="post-title" style="top:92px;font-size:5.6px;line-height:10px">Temporibus autem<b>quibusdam et aut officiis</b></p><p class="post-excerpt" style="top:113px;font-size:4.4px;line-height:9px">debitis aut rerum nece ssitatib<br>saepe eveniet voluptates</p><span class="post-arrow" style="top:130px;font-size:9px">&#8594;</span></article>
      <article class="post-card" style="left:190px;top:68px;width:88px;height:152px"><div class="post-photo photo-2" role="img" aria-label="Show jumping arena with poles" style="top:4px;width:80px;height:80px"></div><div class="post-date" style="top:74px;width:15px;height:15px">15 sep<br>2021</div><p class="post-title" style="top:92px;font-size:5.6px;line-height:10px">Temporibus autem<b>quibusdam et aut officiis</b></p><p class="post-excerpt" style="top:113px;font-size:4.4px;line-height:9px">debitis aut rerum nece ssitatib<br>saepe eveniet voluptates</p><span class="post-arrow" style="top:130px;font-size:9px">&#8594;</span></article>
      <article class="post-card" style="left:303px;top:68px;width:88px;height:152px"><div class="post-photo photo-3" role="img" aria-label="Person grooming a brown horse" style="top:4px;width:80px;height:80px"></div><div class="post-date" style="top:74px;width:15px;height:15px">15 sep<br>2021</div><p class="post-title" style="top:92px;font-size:5.6px;line-height:10px">Temporibus autem<b>quibusdam et aut officiis</b></p><p class="post-excerpt" style="top:113px;font-size:4.4px;line-height:9px">debitis aut rerum nece ssitatib<br>saepe eveniet voluptates</p><span class="post-arrow" style="top:130px;font-size:9px">&#8594;</span></article>
      <article class="post-card" style="left:77px;top:230px;width:88px;height:152px"><div class="post-photo photo-4" role="img" aria-label="Rider resting against a chestnut horse" style="top:4px;width:80px;height:80px"></div><div class="post-date" style="top:74px;width:15px;height:15px">15 sep<br>2021</div><p class="post-title" style="top:92px;font-size:5.6px;line-height:10px">Temporibus autem<b>quibusdam et aut officiis</b></p><p class="post-excerpt" style="top:113px;font-size:4.4px;line-height:9px">debitis aut rerum nece ssitatib<br>saepe eveniet voluptates</p><span class="post-arrow" style="top:130px;font-size:9px">&#8594;</span></article>
      <article class="post-card" style="left:190px;top:230px;width:88px;height:152px"><div class="post-photo photo-5" role="img" aria-label="Close view of a horse head with bridle" style="top:4px;width:80px;height:80px"></div><div class="post-date" style="top:74px;width:15px;height:15px">15 sep<br>2021</div><p class="post-title" style="top:92px;font-size:5.6px;line-height:10px">Temporibus autem<b>quibusdam et aut officiis</b></p><p class="post-excerpt" style="top:113px;font-size:4.4px;line-height:9px">debitis aut rerum nece ssitatib<br>saepe eveniet voluptates</p><span class="post-arrow" style="top:130px;font-size:9px">&#8594;</span></article>
      <article class="post-card" style="left:303px;top:230px;width:88px;height:152px"><div class="post-photo photo-6" role="img" aria-label="Rider leaning over a grey horse" style="top:4px;width:80px;height:80px"></div><div class="post-date" style="top:74px;width:15px;height:15px">15 sep<br>2021</div><p class="post-title" style="top:92px;font-size:5.6px;line-height:10px">Temporibus autem<b>quibusdam et aut officiis</b></p><p class="post-excerpt" style="top:113px;font-size:4.4px;line-height:9px">debitis aut rerum nece ssitatib<br>saepe eveniet voluptates</p><span class="post-arrow" style="top:130px;font-size:9px">&#8594;</span></article>
    </div>
    <svg class="wave" style="top:935px" width="460" height="75" viewBox="0 0 460 75">
      <path d="M0 75 L0 30 C70 34 120 48 165 58 C215 44 290 18 460 24 L460 75Z" fill="#0b0b0b"/>
      <path d="M0 30 C70 34 120 48 165 58 C215 44 290 18 460 24" fill="none" stroke="#1b1b1b" stroke-width="3"/>
    </svg>
    <div class="footer" style="top:1005px;height:169px">
      <h4 class="footer-heading" style="left:67px;top:22px;font-size:7.5px">Useful Links</h4>
      <div class="footer-links" style="left:68px;top:42px;font-size:4.6px;line-height:12.5px"><a>Home</a><a>About</a><a>Services</a><a>Blog</a><a>Contact</a></div>
      <div class="divider-v" style="left:135px;top:10px;height:120px"></div>
      <div class="footer-brand" style="left:145px;top:30px;width:150px;font-size:8px"><i style="width:36px;height:36px"></i>The Wandering Mentor</div>
      <div class="divider-v" style="left:302px;top:10px;height:120px"></div>
      <div class="footer-contact" style="left:317px;top:18px;width:125px;font-size:4.4px;line-height:9px">
        <p>Lorem ipsum dolor sit amet, consectetur adipiscing elit, sed do eiusmod tempor incididunt ut labore et dolore magna aliqua.</p>
        <p style="margin-top:8px"><span class="icon">&#9679;</span>48 Harbour Lane, Fitzroy,<br>&nbsp;&nbsp;&nbsp;Melbourne, Australia.</p>
        <p style="margin-top:4px"><span class="icon">&#9742;</span>555-014-2290</p>
        <p style="margin-top:4px"><span class="icon">&#9993;</span>info@TheWanderingMentor.com</p>
      </div>
      <div class="divider-h" style="left:55px;top:137px;width:340px"></div>
      <p class="legal" style="left:57px;top:150px">Privacy Policy</p>
      <p class="legal" style="left:202px;top:150px">© 2021 All Rights Reserved</p>
      <p class="legal" style="left:365px;top:150px">Terms &amp; Conditions</p>
    </div>
  </section>

  <!-- Desktop layout B -->
  <section class="page page--desktop page--b">
    <div class="top-bar">
      <i class="social" style="left:55px"></i><i class="social" style="left:66px"></i><i class="social" style="left:77px"></i>
      <div class="contact-line"><span>Phone: 555-014-2290</span><span>Email: hello@wanderingmentor.demo</span></div>
    </div>
    <div class="brand-badge"><i></i>The Wandering Mentor</div>
    <nav class="main-nav"><a class="is-active">HOME</a><a>ABOUT</a><a>SERVICES</a><a>BLOGS</a><a>FAQS</a><a>BOOKINGS</a></nav>
    <h2 class="hero-title">THE WANDERING MENTOR</h2>
    <p class="hero-sub">Partnering With Academic Advisors In Moving Their Practice Forward</p>
    <div class="slider-dots" style="top:237px"><i></i><i class="on"></i><i></i><i></i></div>
    <svg class="wave" style="top:250px" width="460" height="70" viewBox="0 0 460 70">
      <path d="M0 70 L0 18 C120 25 280 45 460 5 L460 70Z" fill="#1d1b1c"/>
      <path d="M0 18 C120 25 280 45 460 5 L460 0 C300 30 140 12 0 4Z" fill="#d7a964"/>
    </svg>
    <div class="welcome" style="top:300px;height:218px">
      <div class="welcome-art" role="img" aria-label="Line illustration of a horse and rider jumping" style="left:28px;top:30px;width:210px;height:140px"></div>
      <p class="eyebrow" style="left:252px;top:25px;font-size:10.5px">WELCOME TO</p>
      <h3 class="welcome-heading" style="left:252px;top:41px;font-size:10.5px">THE WANDERING MENTOR</h3>
      <div class="rule" style="left:252px;top:58px"></div>
      <p class="welcome-copy" style="left:252px;top:71px;width:182px;font-size:4.9px;line-height:10.7px">I started The Wandering Mentor in 2021 to write about the practice of academic advising through the lens of horsemanship. After one year of developing skills as a brand new equestrian, I couldn't help but notice the similarities between my vocation as an academic advisor and my avocation as a budding equestrian. I hope my musings about my journey in two very different fields will cultivate curiosity, widen your aperture and ignite academic advisors to take their practice to the next level.</p>
      <div class="btn" style="left:252px;top:163px;width:68px;height:19px;line-height:19px;font-size:5.2px">LEARN MORE</div>
    </div>
    <div class="blog" style="top:518px;height:430px">
      <h3 class="blog-heading" style="top:30px;font-size:11.5px">OUR LATEST BLOG</h3>
      <div class="rule rule--dark" style="left:219px;top:48px"></div>

      <article class="post-card" style="left:77px;top:66px;width:88px;height:152px"><div class="post-photo photo-1" role="img" aria-label="Rider hugging a horse" style="top:4px;width:80px;height:80px"></div><div class="post-date" style="top:74px;width:15px;height:15px">15 sep<br>2021</div><p class="post-title" style="top:92px;font-size:5.6px;line-height:10px">Temporibus autem<b>quibusdam et aut officiis</b></p><p class="post-excerpt" style="top:113px;font-size:4.4px;line-height:9px">debitis aut rerum nece ssitatib<br>saepe eveniet voluptates</p><span class="post-arrow" style="top:130px;font-size:9px">&#8594;</span></article>
      <article class="post-card" style="left:190px;top:66px;width:88px;height:152px"><div class="post-photo photo-2" role="img" aria-label="Show jumping arena with poles" style="top:4px;width:80px;height:80px"></div><div class="post-date" style="top:74px;width:15px;height:15px">15 sep<br>2021</div><p class="post-title" style="top:92px;font-size:5.6px;line-height:10px">Temporibus autem<b>quibusdam et aut officiis</b></p><p class="post-excerpt" style="top:113px;font-size:4.4px;line-height:9px">debitis aut rerum nece ssitatib<br>saepe eveniet voluptates</p><span class="post-arrow" style="top:130px;font-size:9px">&#8594;</span></article>
      <article class="post-card" style="left:303px;top:66px;width:88px;height:152px"><div class="post-photo photo-3" role="img" aria-label="Person grooming a brown horse" style="top:4px;width:80px;height:80px"></div><div class="post-date" style="top:74px;width:15px;height:15px">15 sep<br>2021</div><p class="post-title" style="top:92px;font-size:5.6px;line-height:10px">Temporibus autem<b>quibusdam et aut officiis</b></p><p class="post-excerpt" style="top:113px;font-size:4.4px;line-height:9px">debitis aut rerum nece ssitatib<br>saepe eveniet voluptates</p><span class="post-arrow" style="top:130px;font-size:9px">&#8594;</span></article>
      <article class="post-card" style="left:77px;top:229px;width:88px;height:152px"><div class="post-photo photo-4" role="img" aria-label="Rider resting against a chestnut horse" style="top:4px;width:80px;height:80px"></div><div class="post-date" style="top:74px;width:15px;height:15px">15 sep<br>2021</div><p class="post-title" style="top:92px;font-size:5.6px;line-height:10px">Temporibus autem<b>quibusdam et aut officiis</b></p><p class="post-excerpt" style="top:113px;font-size:4.4px;line-height:9px">debitis aut rerum nece ssitatib<br>saepe eveniet voluptates</p><span class="post-arrow" style="top:130px;font-size:9px">&#8594;</span></article>
      <article class="post-card" style="left:190px;top:229px;width:88px;height:152px"><div class="post-photo photo-5" role="img" aria-label="Close view of a horse head with bridle" style="top:4px;width:80px;height:80px"></div><div class="post-date" style="top:74px;width:15px;height:15px">15 sep<br>2021</div><p class="post-title" style="top:92px;font-size:5.6px;line-height:10px">Temporibus autem<b>quibusdam et aut officiis</b></p><p class="post-excerpt" style="top:113px;font-size:4.4px;line-height:9px">debitis aut rerum nece ssitatib<br>saepe eveniet voluptates</p><span class="post-arrow" style="top:130px;font-size:9px">&#8594;</span></article>
      <article class="post-card" style="left:303px;top:229px;width:88px;height:152px"><div class="post-photo photo-6" role="img" aria-label="Rider leaning over a grey horse" style="top:4px;width:80px;height:80px"></div><div class="post-date" style="top:74px;width:15px;height:15px">15 sep<br>2021</div><p class="post-title" style="top:92px;font-size:5.6px;line-height:10px">Temporibus autem<b>quibusdam et aut officiis</b></p><p class="post-excerpt" style="top:113px;font-size:4.4px;line-height:9px">debitis aut rerum nece ssitatib<br>saepe eveniet voluptates</p><span class="post-arrow" style="top:130px;font-size:9px">&#8594;</span></article>
    </div>
    <svg class="wave" style="top:920px" width="460" height="60" viewBox="0 0 460 60">
      <path d="M0 60 L0 25 C120 10 300 5 460 30 L460 60Z" fill="#0b0b0b"/>
      <path d="M0 25 C120 10 300 5 460 30" fill="none" stroke="#2a2a2a" stroke-width="3"/>
    </svg>
    <div class="footer" style="top:975px;height:199px">
      <h4 class="footer-heading" style="left:67px;top:40px;font-size:7.5px">Useful Links</h4>
      <div class="footer-links" style="left:68px;top:60px;font-size:4.6px;line-height:12.5px"><a>Home</a><a>About</a><a>Services</a><a>Blog</a><a>Contact</a></div>
      <div class="divider-v" style="left:135px;top:28px;height:120px"></div>
      <div class="footer-brand" style="left:145px;top:48px;width:140px;font-size:8px"><i style="width:36px;height:36px"></i>The Wandering Mentor</div>
      <div class="divider-v" style="left:292px;top:28px;height:120px"></div>
      <div class="footer-contact" style="left:317px;top:36px;width:125px;font-size:4.4px;line-height:9px">
        <p>Lorem ipsum dolor sit amet, consectetur adipiscing elit, sed do eiusmod tempor incididunt ut labore et dolore magna aliqua.</p>
        <p style="margin-top:8px"><span class="icon">&#9679;</span>48 Harbour Lane, Fitzroy,<br>&nbsp;&nbsp;&nbsp;Melbourne, Australia.</p>
        <p style="margin-top:4px"><span class="icon">&#9742;</span>555-014-2290</p>
        <p style="margin-top:4px"><span class="icon">&#9993;</span>info@TheWanderingMentor.com</p>
      </div>
      <div class="divider-h" style="left:55px;top:155px;width:352px"></div>
      <p class="legal" style="left:57px;top:167px">Privacy Policy</p>
      <p class="legal" style="left:202px;top:167px">© 2021 All Rights Reserved</p>
      <p class="legal" style="left:365px;top:167px">Terms &amp; Conditions</p>
    </div>
  </section>

  <!-- Mobile layout -->
  <section class="page page--mobile">
    <div class="top-bar" style="height:40px">
      <i class="social" style="left:10px;width:7px;height:7px"></i><i class="social" style="left:19px;width:7px;height:7px"></i><i class="social" style="left:28px;width:7px;height:7px"></i>
      <span style="right:6px;top:1px;color:var(--gold);font-size:7px">&#8801;</span>
    </div>
    <div class="brand-badge" style="top:22px;font-size:4.4px"><i style="width:5px;height:5px"></i>The Wandering Mentor</div>
    <h2 class="hero-title" style="top:60px;font-size:6.8px">THE WANDERING MENTOR</h2>
    <p class="hero-sub" style="top:74px;font-size:2.4px">Partnering With Academic Advisors In Moving Their Practice Forward</p>
    <svg class="wave" style="top:102px" width="127" height="30" viewBox="0 0 127 30">
      <path d="M0 30 L0 24 C30 22 50 10 64 8 C80 8 100 20 127 24 L127 30Z" fill="#1d1b1c"/>
      <path d="M0 24 C30 22 50 10 64 8 C80 8 100 20 127 24" fill="none" stroke="#d7a964" stroke-width="1.5"/>
    </svg>
    <div class="welcome" style="top:130px;height:275px">
      <p class="eyebrow" style="left:0;width:100%;text-align:center;top:14px;font-size:6.2px">WELCOME TO</p>
      <h3 class="welcome-heading" style="left:0;width:100%;text-align:center;top:23px;font-size:6.2px">THE WANDERING MENTOR</h3>
      <div class="rule" style="left:53px;top:35px"></div>
      <div class="welcome-art" role="img" aria-label="Line illustration of a horse and rider jumping" style="left:18px;top:48px;width:92px;height:68px"></div>
      <p class="welcome-copy" style="left:12px;top:120px;width:103px;text-align:center;font-size:3.3px;line-height:7.6px">I started The Wandering Mentor in 2021 to write about the practice of academic advising through the lens of horsemanship. After one year of developing skills as a brand new equestrian, I couldn't help but notice the similarities between my vocation as an academic advisor and my avocation as a budding equestrian. I hope my musings about my journey in two very different fields will cultivate curiosity, widen your aperture and ignite academic advisors to take their practice to the next level.</p>
      <div class="btn" style="left:41px;top:238px;width:45px;height:12px;line-height:12px;font-size:3.4px">LEARN MORE</div>
    </div>
    <div class="blog" style="top:405px;height:1010px">
      <h3 class="blog-heading" style="top:18px;font-size:6.2px">OUR LATEST BLOG</h3>
      <div class="rule rule--dark" style="left:55px;top:29px;width:18px"></div>

      <article class="post-card" style="left:24px;top:42px;width:80px;height:140px;border-radius:40px"><div class="post-photo photo-1" role="img" aria-label="Rider hugging a horse" style="top:4px;width:72px;height:72px"></div><div class="post-date" style="top:66px;width:13px;height:13px">15 sep<br>2021</div><p class="post-title" style="top:82px;font-size:5px;line-height:9px">Temporibus autem<b>quibusdam et aut officiis</b></p><p class="post-excerpt" style="top:101px;font-size:3.9px;line-height:8px">debitis aut rerum nece ssitatib<br>saepe eveniet voluptates</p><span class="post-arrow" style="top:118px;font-size:8px">&#8594;</span></article>
      <article class="post-card" style="left:24px;top:199px;width:80px;height:140px;border-radius:40px"><div class="post-photo photo-2" role="img" aria-label="Show jumping arena with poles" style="top:4px;width:72px;height:72px"></div><div class="post-date" style="top:66px;width:13px;height:13px">15 sep<br>2021</div><p class="post-title" style="top:82px;font-size:5px;line-height:9px">Temporibus autem<b>quibusdam et aut officiis</b></p><p class="post-excerpt" style="top:101px;font-size:3.9px;line-height:8px">debitis aut rerum nece ssitatib<br>saepe eveniet voluptates</p><span class="post-arrow" style="top:118px;font-size:8px">&#8594;</span></article>
      <article class="post-card" style="left:24px;top:356px;width:80px;height:140px;border-radius:40px"><div class="post-photo photo-3" role="img" aria-label="Person grooming a brown horse" style="top:4px;width:72px;height:72px"></div><div class="post-date" style="top:66px;width:13px;height:13px">15 sep<br>2021</div><p class="post-title" style="top:82px;font-size:5px;line-height:9px">Temporibus autem<b>quibusdam et aut officiis</b></p><p class="post-excerpt" style="top:101px;font-size:3.9px;line-height:8px">debitis aut rerum nece ssitatib<br>saepe eveniet voluptates</p><span class="post-arrow" style="top:118px;font-size:8px">&#8594;</span></article>
      <article class="post-card" style="left:24px;top:513px;width:80px;height:140px;border-radius:40px"><div class="post-photo photo-4" role="img" aria-label="Rider resting against a chestnut horse" style="top:4px;width:72px;height:72px"></div><div class="post-date" style="top:66px;width:13px;height:13px">15 sep<br>2021</div><p class="post-title" style="top:82px;font-size:5px;line-height:9px">Temporibus autem<b>quibusdam et aut officiis</b></p><p class="post-excerpt" style="top:101px;font-size:3.9px;line-height:8px">debitis aut rerum nece ssitatib<br>saepe eveniet voluptates</p><span class="post-arrow" style="top:118px;font-size:8px">&#8594;</span></article>
      <article class="post-card" style="left:24px;top:670px;width:80px;height:140px;border-radius:40px"><div class="post-photo photo-5" role="img" aria-label="Close view of a horse head with bridle" style="top:4px;width:72px;height:72px"></div><div class="post-date" style="top:66px;width:13px;height:13px">15 sep<br>2021</div><p class="post-title" style="top:82px;font-size:5px;line-height:9px">Temporibus autem<b>quibusdam et aut officiis</b></p><p class="post-excerpt" style="top:101px;font-size:3.9px;line-height:8px">debitis aut rerum nece ssitatib<br>saepe eveniet voluptates</p><span class="post-arrow" style="top:118px;font-size:8px">&#8594;</span></article>
      <article class="post-card" style="left:24px;top:827px;width:80px;height:140px;border-radius:40px"><div class="post-photo photo-6" role="img" aria-label="Rider leaning over a grey horse" style="top:4px;width:72px;height:72px"></div><div class="post-date" style="top:66px;width:13px;height:13px">15 sep<br>2021</div><p class="post-title" style="top:82px;font-size:5px;line-height:9px">Temporibus autem<b>quibusdam et aut officiis</b></p><p class="post-excerpt" style="top:101px;font-size:3.9px;line-height:8px">debitis aut rerum nece ssitatib<br>saepe eveniet voluptates</p><span class="post-arrow" style="top:118px;font-size:8px">&#8594;</span></article>
    </div>
    <svg class="wave" style="top:1395px" width="127" height="25" viewBox="0 0 127 25">
      <path d="M0 25 L0 14 C40 16 70 4 127 10 L127 25Z" fill="#0b0b0b"/>
    </svg>
    <div class="footer" style="top:1418px;height:430px">
      <div class="footer-contact" style="left:8px;top:30px;width:111px;text-align:center;font-size:3.6px;line-height:8.5px">
        <p>Lorem ipsum dolor sit amet, consectetur adipiscing elit, sed do eiusmod tempor incididunt ut labore et dolore magna aliqua.</p>
        <p style="margin-top:6px"><span class="icon">&#9679;</span>48 Harbour Lane, Fitzroy,<br>Melbourne, Australia.</p>
        <p style="margin-top:3px"><span class="icon">&#9742;</span>555-014-2290</p>
        <p style="margin-top:3px"><span class="icon">&#9993;</span>info@TheWanderingMentor.com</p>
      </div>
      <div class="footer-brand" style="left:0;top:140px;width:127px;font-size:6.5px"><i style="width:34px;height:34px"></i>The Wandering Mentor</div>
      <div class="divider-h" style="left:0;top:250px;width:127px"></div>
      <h4 class="footer-heading" style="left:0;width:127px;text-align:center;top:273px;font-size:6.6px">Useful Links</h4>
      <div class="footer-links" style="left:0;width:127px;text-align:center;top:290px;font-size:3.8px;line-height:11px"><a>Home</a><a>About</a><a>Services</a><a>Blog</a><a>Contact</a></div>
      <div class="divider-h" style="left:0;top:365px;width:127px"></div>
      <p class="legal" style="left:0;width:127px;text-align:center;top:372px;font-size:3.6px;line-height:8.5px;white-space:normal">© 2021 All Rights Reserved<br>Terms &amp; Conditions<br>Privacy Policy</p>
    </div>
  </section>

</div>
</body>
</html>
```